I need a very simple poster with the following quote:
"Cada escolha, uma renĂșncia, isso Ă© a vida"
Which means that to every choice there is a waiver, that's life.

It will be framed and used in my living room.

The poster has to be black and white. It is not mandatory to use commas and quotes.

The design has to be modern, like the references I posted on this board: http://pinboardly.example/marvetu/ideas/

```html
<!DOCTYPE html>
<html lang="pt">
<head>
<meta charset="utf-8">
<title>Cada escolha, uma renúncia, isso é a vida</title>
<link rel="stylesheet" href="https://fonts.googleapis.com/css2?family=Jost:wght@400&display=swap">
<style>
  :root {
    --ink: #000000;
    --paper: #ffffff;
  }
  html, body {
    margin: 0;
    padding: 0;
    width: 849px;
    height: 1200px;
    overflow: hidden;
    background: var(--ink);
  }
  .poster {
    display: block;
    width: 849px;
    height: 1200px;
    background: var(--ink);
  }
  .rule { fill: var(--paper); }
  .quote-line {
    fill: var(--paper);
    font-family: "Jost", "Futura", sans-serif;
    font-weight: 400;
    font-size: 52px;
    letter-spacing: 6.2px;
  }
</style>
</head>
<body>
<svg class="poster" viewBox="0 0 849 1200" xmlns="http://www.w3.org/2000/svg" role="img" aria-label="Cada escolha, uma renúncia, isso é a vida">
  <g class="rules">
    <rect class="rule rule--thin" x="0" y="133" width="849" height="3"/>
    <rect class="rule rule--thin" x="0" y="154" width="849" height="3"/>
    <rect class="rule rule--bold" x="0" y="285" width="849" height="5"/>
    <rect class="rule rule--bold" x="0" y="427" width="849" height="5"/>
    <rect class="rule rule--bold" x="0" y="569" width="849" height="5"/>
    <rect class="rule rule--bold" x="0" y="710" width="849" height="5"/>
    <rect class="rule rule--thin" x="0" y="845" width="849" height="3"/>
    <rect class="rule rule--thin" x="0" y="866" width="849" height="3"/>
  </g>
  <g class="quote">
    <text class="quote-line" x="53" y="385">CADA ESCOLHA</text>
    <text class="quote-line" x="53" y="526">UMA RENÚNCIA</text>
    <text class="quote-line" x="53" y="665">ISSO É A VIDA</text>
  </g>
</svg>
</body>
</html>
```